Modern Business Card Design Needed for Young Realtor

Information that is going on the card:Marvin Pold
Broker/Owner
555.210.3367
Marvin@MPoldRealty.com
www.MPoldRealty.com

Would also like to include my Instagram Handle somewhere. Probably on the back: the_queencity_realtorMy previous business card is attached, I like that one but would like an updated version and maybe a few design changes

Marvin Pold
Broker/Owner
555.210.3367
Marvin@MPoldRealty.com
www.MPoldRealty.com

• Would also like to include my Instagram Handle somewhere. Probably on the back: the_pinecrest_realtor
• Dorrance Hale or the DH (logo from the previous card.)

```html
<!DOCTYPE html>
<html lang="en">
<head>
<meta charset="utf-8">
<title>MPold Realty Business Card</title>
<link href="https://fonts.googleapis.com/css2?family=Arimo:wght@400;700&family=Arvo:wght@700&display=swap" rel="stylesheet">
<style>
  :root {
    --brand-red: #ad2230;
    --ink: #1e1e1e;
    --charcoal: #3a3332;
    --paper: #ffffff;
    --stage-dark: #2a2b2d;
    --stage-light: #4a4c50;
  }
  * { margin: 0; padding: 0; box-sizing: border-box; }
  html, body { width: 1200px; height: 900px; overflow: hidden; }
  body {
    background: radial-gradient(circle at 60% 25%, var(--stage-light), var(--stage-dark) 70%);
    font-family: "Arimo", Arial, sans-serif;
    position: relative;
  }
  .card {
    position: absolute;
    width: 620px;
    height: 354px;
    border-radius: 26px;
    overflow: hidden;
    box-shadow: 0 14px 30px rgba(0,0,0,0.45);
  }
  .card-back { left: 290px; top: 50px; background: var(--brand-red); }
  .card-front { left: 290px; top: 460px; background: var(--paper); }

  .wordmark {
    display: flex; align-items: center; gap: 10px;
    font-family: "Arimo", Arial, sans-serif;
    font-weight: 400;
    letter-spacing: 0.28em;
    text-transform: uppercase;
    white-space: nowrap;
  }
  .wordmark-square { flex: none; }

  .card-back .wordmark {
    position: absolute; left: 0; right: 0; top: 120px;
    justify-content: center; font-size: 40px; color: var(--paper);
  }
  .card-back .wordmark-square { background: var(--paper); width: 18px; height: 18px; }
  .card-back .wordmark-rule {
    position: absolute; left: 150px; right: 150px; top: 176px;
    height: 1px; background: var(--paper);
  }
  .back-handle {
    position: absolute; left: 0; right: 0; top: 250px;
    text-align: center; color: var(--paper); font-size: 15px; letter-spacing: 0.02em;
  }

  .portrait {
    position: absolute; left: 60px; top: 40px; width: 250px; height: 314px;
    background: linear-gradient(180deg, #f4f4f4 0%, #d9d4d1 35%, #7a7a7c 70%, #6a6b6e 100%);
  }
  .front-wave { position: absolute; left: 0; top: 224px; width: 620px; height: 130px; }

  .front-info { position: absolute; left: 330px; top: 28px; width: 270px; }
  .front-info .wordmark { font-size: 21px; letter-spacing: 0.2em; color: var(--ink); gap: 8px; line-height: 26px; }
  .front-info .wordmark-square { background: var(--brand-red); width: 13px; height: 13px; }
  .wordmark-rule-dark { height: 1px; background: var(--charcoal); margin-top: 6px; width: 240px; }
  .wordmark-rule-red { height: 1px; background: var(--brand-red); margin-top: 16px; width: 270px; opacity: 0.8; }
  .agent-name {
    font-family: "Arvo", Georgia, serif; font-weight: 700;
    color: var(--brand-red); font-size: 26px; line-height: 32px; margin-top: 10px;
  }
  .agent-role { font-size: 14px; line-height: 17px; color: var(--ink); }
  .contact-rule { height: 1px; background: var(--brand-red); width: 230px; margin-top: 8px; opacity: 0.8; }
  .contact-list { list-style: none; margin-top: 8px; }
  .contact-list li {
    display: flex; align-items: center; gap: 8px;
    font-size: 13.5px; color: var(--ink); line-height: 20px;
  }
  .contact-icon { width: 11px; height: 11px; flex: none; }
  .accent { color: var(--brand-red); }
  .social-handle {
    position: absolute; right: 44px; bottom: 30px;
    display: flex; align-items: center; gap: 8px;
    color: var(--paper); font-size: 14px;
  }
  .social-dot { width: 12px; height: 12px; border: 1.5px solid var(--paper); border-radius: 3px; }
</style>
</head>
<body>

<section class="card card-back" aria-label="Card back">
  <div class="wordmark"><span class="wordmark-square"></span>MPold Realty</div>
  <div class="wordmark-rule"></div>
  <p class="back-handle">the_pinecrest_realtor</p>
</section>

<section class="card card-front" aria-label="Card front">
  <div class="portrait" role="img" aria-label="Portrait photo of the broker in a grey blazer and white shirt"></div>

  <svg class="front-wave" viewBox="0 0 620 130" preserveAspectRatio="none" aria-hidden="true">
    <path d="M0 114 C170 106 280 89 370 44 C440 12 530 2 620 -2 L620 130 L0 130 Z" fill="var(--charcoal)"/>
    <path d="M0 110 C170 102 280 85 370 40 C440 8 530 -2 620 -6 L620 -2 C530 2 440 12 370 44 C280 89 170 106 0 114 Z" fill="var(--paper)"/>
    <path d="M0 120 C170 112 280 95 370 50 C440 18 530 8 620 4 L620 130 L0 130 Z" fill="var(--brand-red)"/>
  </svg>

  <div class="front-info">
    <div class="wordmark"><span class="wordmark-square"></span>MPold Realty</div>
    <div class="wordmark-rule-dark"></div>
    <div class="wordmark-rule-red"></div>
    <h1 class="agent-name">Marvin Pold</h1>
    <p class="agent-role">Broker/Owner</p>
    <div class="contact-rule"></div>
    <ul class="contact-list">
      <li>
        <svg class="contact-icon" viewBox="0 0 12 12" aria-hidden="true"><path d="M2 1 L4.5 1 L5.5 4 L4 5 C4.8 6.6 5.6 7.4 7 8 L8 6.5 L11 7.5 L11 10 C11 10.6 10.6 11 10 11 C5 11 1 7 1 2 C1 1.4 1.4 1 2 1 Z" fill="var(--brand-red)"/></svg>
        555.210.3367
      </li>
      <li>
        <svg class="contact-icon" viewBox="0 0 12 12" aria-hidden="true"><rect x="1" y="2.5" width="10" height="7" rx="1" fill="var(--brand-red)"/><path d="M1.5 3 L6 6.5 L10.5 3" stroke="var(--paper)" stroke-width="1" fill="none"/></svg>
        Marvin@MPoldRealty.com
      </li>
      <li>
        <svg class="contact-icon" viewBox="0 0 12 12" aria-hidden="true"><circle cx="6" cy="6" r="5" fill="var(--brand-red)"/><path d="M1 6 H11 M6 1 C3.5 3.5 3.5 8.5 6 11 M6 1 C8.5 3.5 8.5 8.5 6 11" stroke="var(--paper)" stroke-width="0.8" fill="none"/></svg>
        <span>www.<span class="accent">MPoldRealty</span>.com</span>
      </li>
    </ul>
  </div>

  <div class="social-handle"><span class="social-dot"></span>@MPoldRealty</div>
</section>

</body>
</html>
```